HARBORLINE AUTO GLASS

Mobile Glass Shop:

1) Windshield REPAIR 2)Windshield replacment 3) Rear Windshield Replacment 4) Side Window Replacment 5) car window replacment 6) Power Window Repair.

Schedual a service within 24 hour with one of our certified technicians.

See "brightvane auto repair" web site for referance on the nature of our buisness and service. www.brightvane-example.com

```html
<!DOCTYPE html>
<html lang="en">
<head>
<meta charset="utf-8">
<title>Harborline Auto Glass</title>
<link href="https://fonts.googleapis.com/css2?family=Montserrat:wght@400;500;600;700&family=Poppins:wght@300;400;500;600;700&display=swap" rel="stylesheet">
<style>
:root{
  --blue:#2196d3;
  --blue-dark:#0a5c99;
  --navy:#114a86;
  --ink:#222;
  --muted:#666;
  --light:#f3f6fb;
  --white:#fff;
}
*{box-sizing:border-box;margin:0;padding:0}
html,body{width:1200px;height:3480px;overflow:hidden}
body{position:relative;background:var(--white);font-family:'Poppins',sans-serif;color:var(--ink)}
.abs{position:absolute}

/* header */
.site-header{position:absolute;left:0;top:0;width:1200px;height:97px;background:var(--white)}
.brand{position:absolute;display:flex;align-items:center;gap:10px;font-family:'Poppins',sans-serif;font-weight:700;color:var(--navy)}
.brand .mark{width:34px;height:34px;background:var(--blue);border-radius:4px}
.site-header .brand{left:108px;top:28px;font-size:17px;line-height:1.1}
.nav a{position:absolute;top:42px;font-family:'Montserrat',sans-serif;font-size:13px;font-weight:500;color:#333;text-decoration:none;letter-spacing:.3px}
.nav a.active{color:var(--navy);font-weight:600}
.nav a.active::after{content:"";position:absolute;left:0;right:0;bottom:-9px;height:2px;background:var(--navy)}
.nav .caret{display:inline-block;margin-left:6px;width:6px;height:6px;border-right:1.5px solid #333;border-bottom:1.5px solid #333;transform:rotate(45deg) translateY(-3px)}
.btn-book{position:absolute;left:921px;top:34px;width:171px;height:34px;border-radius:17px;background:var(--navy);color:var(--white);font-family:'Montserrat',sans-serif;font-size:12px;font-weight:600;display:flex;align-items:center;justify-content:center}

/* hero */
.hero{position:absolute;left:0;top:97px;width:1200px;height:595px;background:linear-gradient(100deg,#3a4148 0%,#6c7884 35%,#8fa0ae 60%,#5d6a76 100%);overflow:hidden}
.hero-circle{position:absolute;left:369px;top:1px;width:494px;height:494px;border-radius:50%;background:rgba(53,170,225,.82);text-align:center;color:var(--white)}
.hero-circle h1{margin-top:165px;font-weight:400;font-size:40px;line-height:46px}
.hero-circle h1 strong{display:block;font-weight:700}
.hero-circle p{margin:14px auto 0;width:420px;font-size:14px;line-height:21px;font-weight:300}
.btn-start{display:inline-flex;margin-top:18px;width:115px;height:33px;border-radius:17px;background:var(--white);color:var(--navy);font-size:11px;font-weight:600;align-items:center;justify-content:center}
.dots{display:flex;justify-content:center;gap:10px;margin-top:18px}
.dots span{width:13px;height:13px;border-radius:50%;background:var(--white)}
.dots span:first-child{background:transparent;border:2px solid var(--white)}

/* services */
.service{position:absolute;width:284px;height:258px;background:var(--white);box-shadow:0 4px 14px rgba(0,0,0,.08);text-align:center}
.service .icon{position:absolute;left:95px;top:-50px;width:94px;height:94px;border-radius:50%;background:var(--blue);display:flex;align-items:center;justify-content:center}
.service h3{margin-top:76px;font-family:'Montserrat',sans-serif;font-weight:500;font-size:22px;color:var(--ink)}
.service p{margin:14px auto 0;width:236px;font-family:'Montserrat',sans-serif;font-size:12.5px;line-height:24.5px;color:var(--muted)}

/* contact */
.contact{position:absolute;left:0;top:1528px;width:1200px;height:557px;background:linear-gradient(120deg,#28a6e4 0%,#1b8dcf 45%,#0a5c99 100%);color:var(--white);text-align:center}
.contact h2{margin-top:60px;font-weight:500;font-size:35px}
.contact .rule{width:66px;height:2px;background:var(--white);margin:6px auto 0}
.contact .lead{margin-top:16px;font-size:18px}
.field{position:absolute;border:2px solid rgba(255,255,255,.85);border-radius:3px;color:var(--white);font-size:16px;padding:12px 12px;text-align:left}
.btn-submit{position:absolute;left:523px;top:453px;width:154px;height:35px;border-radius:18px;background:var(--white);color:var(--navy);font-size:13px;font-weight:600;display:flex;align-items:center;justify-content:center}

.map{position:absolute;left:0;top:2085px;width:1200px;height:424px;background:linear-gradient(135deg,#eceff2,#e2e6ea 60%,#e8ebee)}

/* news */
.news-title{position:absolute;left:0;top:2560px;width:1200px;text-align:center;font-size:35px;font-weight:500;color:var(--navy)}
.news-title::after{content:"";display:block;width:66px;height:2px;background:var(--navy);margin:4px auto 0}
.news{position:absolute;top:2637px;width:297px;height:376px}
.news.featured{background:var(--white);box-shadow:0 4px 16px rgba(0,0,0,.14)}
.news .photo{position:relative;width:297px;height:214px}
.news .date{position:absolute;left:0;bottom:0;padding:4px 16px;background:rgba(33,150,211,.85);color:var(--white);font-size:11px;font-weight:600}
.news h4{margin:22px 28px 0;font-family:'Montserrat',sans-serif;font-size:13px;line-height:15px;font-weight:700;color:#333}
.news p{margin:8px 28px 0;font-size:11.5px;line-height:17px;color:var(--muted)}
.btn-more{display:inline-flex;margin:18px 0 0 28px;width:118px;height:36px;border:2px solid var(--navy);border-radius:18px;color:var(--navy);font-size:11px;font-weight:600;align-items:center;justify-content:center}

/* footer */
.site-footer{position:absolute;left:0;top:3080px;width:1200px;height:400px;background:var(--light)}
.site-footer .brand{left:146px;top:100px;font-size:18px}
.social{position:absolute;left:149px;top:180px;display:flex;gap:14px}
.social span{width:32px;height:32px;border-radius:50%;background:var(--navy)}
.fcol{position:absolute;top:104px;border-left:3px solid var(--navy);padding-left:18px}
.fcol h5{font-size:17px;font-weight:600;color:#1c2b3a;margin-bottom:14px}
.fcol a{display:block;font-size:14px;color:#555;line-height:29px;text-decoration:none}
.contact-item{display:flex;align-items:center;gap:12px;margin-bottom:13px;font-size:10.5px;color:#555;line-height:14px}
.contact-item .ic{flex:0 0 30px;width:30px;height:30px;border-radius:50%;background:var(--navy);display:flex;align-items:center;justify-content:center}
.copyright{position:absolute;left:0;top:340px;width:1200px;border-top:1px solid #dde3ea;padding-top:24px;text-align:center;font-size:12px;color:#888}
</style>
</head>
<body>

<header class="site-header">
  <div class="brand"><span class="mark"></span><span>HARBORLINE<br>AUTO GLASS</span></div>
  <nav class="nav">
    <a class="active" style="left:408px">HOME</a>
    <a style="left:488px">ABOUT US</a>
    <a style="left:592px">OUR SERVICES<span class="caret"></span></a>
    <a style="left:725px">LOCATIONS</a>
    <a style="left:839px">HIRING</a>
  </nav>
  <div class="btn-book">BOOK AN APPOINTMENT</div>
</header>

<section class="hero" role="img" aria-label="Photo of a technician in a workshop holding a clipboard beside a car windshield">
  <div class="hero-circle">
    <h1>WELCOME TO<strong>HARBORLINE AUTO GLASS</strong></h1>
    <p>Lorem ipsum dolor sit amet, consectetur adipiscing elit, sed do eiusmod tempor incididunt ut labore et dolore magna aliqua. Quis ipsum suspendisse ultrices gravida. Risus com-</p>
    <div class="btn-start">GET STARTED</div>
    <div class="dots"><span></span><span></span><span></span><span></span></div>
  </div>
</section>

<!-- services -->
<svg width="0" height="0" style="position:absolute">
  <symbol id="windshield" viewBox="0 0 40 28"><path d="M4 6 Q20 0 36 6 L32 22 Q20 19 8 22 Z" fill="none" stroke="#fff" stroke-width="2.4" stroke-linejoin="round"/><path d="M9 9 Q20 5 31 9" fill="none" stroke="#fff" stroke-width="1.6"/></symbol>
</svg>
<div class="service" style="left:161px;top:817px"><div class="icon"><svg width="46" height="32"><use href="#windshield"/></svg></div><h3>Windshield REPAIR</h3><p>Lorem ipsum dolor sit amet, con-sectetur adipiscing elit, sed do eius-mod tempor incididunt ut labore et dolore magna aliqua. Quis ipsum</p></div>
<div class="service" style="left:474px;top:817px"><div class="icon"><svg width="46" height="32"><use href="#windshield"/></svg></div><h3>Windshield replacment</h3><p>Lorem ipsum dolor sit amet, con-sectetur adipiscing elit, sed do eius-mod tempor incididunt ut labore et dolore magna aliqua. Quis ipsum</p></div>
<div class="service" style="left:786px;top:817px"><div class="icon"><svg width="46" height="32"><use href="#windshield"/></svg></div><h3>Rear Windshield</h3><p>Lorem ipsum dolor sit amet, con-sectetur adipiscing elit, sed do eius-mod tempor incididunt ut labore et dolore magna aliqua. Quis ipsum</p></div>
<div class="service" style="left:161px;top:1163px"><div class="icon"><svg width="46" height="32"><use href="#windshield"/></svg></div><h3>Side Window</h3><p>Lorem ipsum dolor sit amet, con-sectetur adipiscing elit, sed do eius-mod tempor incididunt ut labore et dolore magna aliqua. Quis ipsum</p></div>
<div class="service" style="left:474px;top:1163px"><div class="icon"><svg width="46" height="36" viewBox="0 0 40 32"><path d="M6 4 H34 V26 H6 Z" fill="none" stroke="#fff" stroke-width="2.2"/><path d="M10 8 H26 L30 18 H10 Z" fill="none" stroke="#fff" stroke-width="1.8"/><path d="M8 29 H32" stroke="#fff" stroke-width="2"/></svg></div><h3>car window replacment</h3><p>Lorem ipsum dolor sit amet, con-sectetur adipiscing elit, sed do eius-mod tempor incididunt ut labore et dolore magna aliqua. Quis ipsum</p></div>
<div class="service" style="left:786px;top:1163px"><div class="icon"><svg width="46" height="32"><use href="#windshield"/></svg></div><h3>Power Window Repair</h3><p>Lorem ipsum dolor sit amet, con-sectetur adipiscing elit, sed do eius-mod tempor incididunt ut labore et dolore magna aliqua. Quis ipsum</p></div>

<section class="contact">
  <h2>GET IN TOUCH</h2>
  <div class="rule"></div>
  <p class="lead">Schedual a service within 24 hour with one of our certified technicians.</p>
  <div class="field" style="left:313px;top:177px;width:280px;height:46px">First name</div>
  <div class="field" style="left:606px;top:177px;width:280px;height:46px">First name</div>
  <div class="field" style="left:313px;top:236px;width:280px;height:46px">Email Address</div>
  <div class="field" style="left:606px;top:236px;width:280px;height:46px">Email Address</div>
  <div class="field" style="left:313px;top:294px;width:573px;height:134px">Message</div>
  <div class="btn-submit">SUBMIT NOW</div>
</section>

<div class="map" role="img" aria-label="Street map of the service area with neighbourhoods, roads and landmarks"></div>

<h2 class="news-title">FEATURED NEWS</h2>
<article class="news" style="left:138px">
  <div class="photo" role="img" aria-label="Photo of hands using a drill on a glass panel" style="background:linear-gradient(135deg,#5a5f66,#a8acb0 55%,#3f4247)"><span class="date">DEC 15, 2021</span></div>
  <h4>LOREM IPSUM DOLOR SIT AMET CONSECTETUR ADIPISCING</h4>
  <p>Duis aute irure dolor in reprehenderit in vo-luptate velit esse cillum dolore</p>
  <div class="btn-more">LEARN MORE</div>
</article>
<article class="news featured" style="left:453px">
  <div class="photo" role="img" aria-label="Photo of technicians installing a windshield with suction lifters" style="background:linear-gradient(135deg,#3d6f8f,#9cb7c7 50%,#2c4a5e)"><span class="date">DEC 15, 2021</span></div>
  <h4>LOREM IPSUM DOLOR SIT AMET CONSECTETUR ADIPISCING</h4>
  <p>Duis aute irure dolor in reprehenderit in vo-luptate velit esse cillum dolore</p>
  <div class="btn-more">LEARN MORE</div>
</article>
<article class="news" style="left:773px">
  <div class="photo" role="img" aria-label="Photo of a worker in a hard hat fitting a window frame" style="background:linear-gradient(135deg,#dfe4e6,#f2f1ec 55%,#c9b48a)"><span class="date">DEC 15, 2021</span></div>
  <h4>LOREM IPSUM DOLOR SIT AMET CONSECTETUR ADIPISCING</h4>
  <p>Duis aute irure dolor in reprehenderit in vo-luptate velit esse cillum dolore</p>
  <div class="btn-more">LEARN MORE</div>
</article>

<footer class="site-footer">
  <div class="brand"><span class="mark"></span><span>HARBORLINE<br>AUTO GLASS</span></div>
  <div class="social" aria-label="Social media links"><span></span><span></span><span></span><span></span></div>
  <div class="fcol" style="left:403px">
    <h5>Navigation</h5>
    <a>Home</a><a>About us</a><a>Our Services</a><a>Contact us</a>
  </div>
  <div class="fcol" style="left:643px">
    <h5 style="font-size:14px">Other Links</h5>
    <a>Terms &amp; Conditions</a><a>Prvacy Policy</a>
  </div>
  <div class="fcol" style="left:848px;border-left:3px solid var(--navy);width:240px">
    <h5 style="font-size:14px">Contact Information</h5>
    <div class="contact-item"><span class="ic"><svg width="14" height="16" viewBox="0 0 14 18"><path d="M7 1a6 6 0 0 0-6 6c0 4.5 6 10 6 10s6-5.5 6-10a6 6 0 0 0-6-6z" fill="#fff"/><circle cx="7" cy="7" r="2.2" fill="#114a86"/></svg></span><span>4180 Tidewater Lane, Suite 120, Coral Bay, CA 90000</span></div>
    <div class="contact-item"><span class="ic"><svg width="14" height="14" viewBox="0 0 16 16"><path d="M3 1l3 3-2 2c1 2 3 4 5 5l2-2 3 3-2 3C7 15 1 9 1 3z" fill="#fff"/></svg></span><span>+123 456 7890</span></div>
    <div class="contact-item"><span class="ic"><svg width="14" height="11" viewBox="0 0 16 12"><rect x="1" y="1" width="14" height="10" fill="#fff"/><path d="M1 1l7 6 7-6" fill="none" stroke="#114a86" stroke-width="1.4"/></svg></span><span>info@harborlineglass.example</span></div>
  </div>
  <div class="copyright">© 2022 HARBORLINEAUTOGLASS ALL RIGHT RESERVED</div>
</footer>

</body>
</html>
```